Business Card Design for BrightlaneReach.com

--I need a business card design for my company BrightlaneReach.com

I have attached my logo...I want the brightlane reach logo on the front of the business card, and then I want The Brightlane Chief on the back of it with my information.

I would like to see a light colored background as well as a dark colored background

FRONT:
BRIGHTLANE REACH LOGO
247 E. Pelham Row
5th Floor
San Diego CA 92384
www.BrightlaneReach.com

Advanced Website & App Development
Websites, Apps, Online Voucher Systems

Leading Edge Marketing Services
SMS, VB, SMM, SEM,

BACK:
BRIGHTLANE CHIEF LOGO
Dorian Welker
The Brightlane Chief
Call Or Text: 555-204-3378
Dorian@BrightlaneChief.com
www.BrightlaneChief.com

Target Market(s)

small business owners

Industry/Entity Type

Business Consultant

Contact Information for Business Card

FRONT:
BRIGHTLANE REACH LOGO
247 E. Pelham Row
5th Floor
San Diego CA 92384
www.BrightlaneReach.com

SMS, VB, SMM, SEM,

BACK:
BRIGHTLANE CHIEF LOGO
Dorian Welker
The Brightlane Chief
Dorian@BrightlaneChief.com
www.BrightlaneChief.com

Requirements
Must have
• add this quote on it somewhere, anywhere,preferrably on back
• "The Fastest Way To Success Is To Take Action”
• — Dorian Welker, Brightlane Chief
Nice to have
• open
Should not have
• red

```html
<!DOCTYPE html>
<html lang="en">
<head>
<meta charset="utf-8">
<title>Brightlane Reach – Business Cards</title>
<link href="https://fonts.googleapis.com/css2?family=Lato:wght@400;700;900&display=swap" rel="stylesheet">
<style>
  :root {
    --stage: #1c1c1e;
    --card-light: #ffffff;
    --card-light-edge: #eef0f2;
    --card-dark: #2c2c2f;
    --card-dark-edge: #232326;
    --brand-blue: #1f7fc1;
    --band-blue: #1a78b8;
    --ink-grey: #555b62;
    --soft-grey: #9aa0a6;
    --rule-grey: #8c9096;
    --map-light: #e2e6ea;
    --map-dark: #3a3b3f;
    --white: #ffffff;
  }
  * { box-sizing: border-box; margin: 0; padding: 0; }
  html, body {
    width: 1200px; height: 873px; overflow: hidden;
    background: var(--stage);
    font-family: "Lato", sans-serif;
  }
  .stage { position: relative; width: 1200px; height: 873px; }

  .card {
    position: absolute; width: 520px; height: 298px;
    border-radius: 14px; overflow: hidden;
    box-shadow: 0 14px 30px rgba(0,0,0,.55);
  }

  /* ---------- Light card: Brightlane Chief ---------- */
  .card--chief {
    left: 80px; top: 110px;
    background: linear-gradient(160deg, var(--card-light), var(--card-light-edge));
  }
  .card--chief .world-map {
    position: absolute; left: 40px; top: 40px; width: 400px; height: 190px;
    border-radius: 40px;
    background: radial-gradient(ellipse at center, var(--map-light) 0%, rgba(226,230,234,0) 70%);
  }
  .chief-name-mark {
    position: absolute; left: 150px; top: 46px; width: 330px; text-align: center;
    font-weight: 900; font-size: 34px; letter-spacing: 3px; color: var(--brand-blue);
  }
  .chief-identity {
    position: absolute; left: 30px; top: 138px; width: 200px; text-align: right;
  }
  .chief-identity .person { font-weight: 900; font-size: 19px; color: var(--brand-blue); }
  .chief-identity .title { font-size: 14px; color: var(--ink-grey); margin-top: 3px; }
  .chief-divider {
    position: absolute; left: 248px; top: 118px; width: 2px; height: 92px;
    background: linear-gradient(to bottom, rgba(140,144,150,0), var(--rule-grey), rgba(140,144,150,0));
  }
  .chief-contact { position: absolute; left: 266px; top: 122px; list-style: none; }
  .chief-contact li {
    display: flex; align-items: center; gap: 8px;
    font-size: 13px; color: var(--ink-grey); height: 26px;
  }
  .chief-contact svg { width: 14px; height: 14px; fill: var(--ink-grey); }
  .quote-band {
    position: absolute; left: 0; bottom: 0; width: 100%; height: 44px;
    background: var(--band-blue);
    display: flex; align-items: center; justify-content: center;
    color: var(--white); font-weight: 700; font-size: 15px;
  }

  /* ---------- Dark card: Brightlane Reach ---------- */
  .card--reach {
    left: 600px; top: 460px;
    background: linear-gradient(160deg, var(--card-dark), var(--card-dark-edge));
  }
  .card--reach .world-map {
    position: absolute; left: 40px; top: 60px; width: 440px; height: 150px;
    border-radius: 40px;
    background: radial-gradient(ellipse at center, var(--map-dark) 0%, rgba(58,59,63,0) 70%);
  }
  .reach-name-mark {
    position: absolute; left: 0; top: 30px; width: 100%; text-align: center;
    font-weight: 900; font-size: 38px; letter-spacing: 3px; color: var(--brand-blue);
  }
  .reach-rule {
    position: absolute; left: 110px; top: 88px; width: 300px; height: 1px;
    background: var(--rule-grey);
  }
  .services { position: absolute; top: 112px; color: var(--brand-blue); font-weight: 700; font-size: 14px; line-height: 1.6; }
  .services--dev { left: 26px; width: 250px; text-align: right; }
  .services--mkt { left: 302px; width: 200px; }
  .services-divider {
    position: absolute; left: 288px; top: 108px; width: 1px; height: 62px;
    background: linear-gradient(to bottom, rgba(140,144,150,0), var(--rule-grey), rgba(140,144,150,0));
  }
  .reach-address {
    position: absolute; left: 0; top: 208px; width: 100%; text-align: center;
    color: var(--white); font-weight: 900; font-size: 16px; line-height: 1.55;
  }
  .reach-address .site-name { color: var(--brand-blue); }
  .reach-rule--foot { top: 262px; left: 90px; width: 340px; }
</style>
</head>
<body>
<main class="stage">

  <section class="card card--chief" aria-label="Brightlane Chief card">
    <div class="world-map" role="img" aria-label="Faint dotted world map"></div>
    <div class="chief-name-mark">BRIGHTLANE CHIEF</div>
    <div class="chief-identity">
      <p class="person">Dorian Welker</p>
      <p class="title">The Brightlane Chief</p>
    </div>
    <div class="chief-divider"></div>
    <ul class="chief-contact">
      <li><svg viewBox="0 0 16 16" aria-hidden="true"><path d="M2 3h12v3c0 1-1 1-2 1h-1l-1-2H6L5 7H4C3 7 2 7 2 6zM4 8h8l2 5H2z"/></svg>555-204-3378</li>
      <li><svg viewBox="0 0 16 16" aria-hidden="true"><path d="M1 3h14v10H1zM2 4v1l6 4 6-4V4z" fill-rule="evenodd"/></svg>Dorian@BrightlaneChief.com</li>
      <li><svg viewBox="0 0 16 16" aria-hidden="true"><path d="M6 10l4-4M7 4l2-2a3 3 0 014 4l-2 2M9 12l-2 2a3 3 0 01-4-4l2-2" stroke="currentColor" stroke-width="1.8" fill="none" style="color:var(--ink-grey)"/></svg>www.BrightlaneChief.com</li>
    </ul>
    <div class="quote-band">The Fastest Way To Success Is To Take Action</div>
  </section>

  <section class="card card--reach" aria-label="Brightlane Reach card">
    <div class="world-map" role="img" aria-label="Faint dotted world map"></div>
    <div class="reach-name-mark">BRIGHTLANE REACH</div>
    <div class="reach-rule"></div>
    <div class="services services--dev">
      <p>Advanced Website &amp; App Development</p>
      <p>Websites, Apps, Online Voucher Systems</p>
    </div>
    <div class="services-divider"></div>
    <div class="services services--mkt">
      <p>Leading Edge Marketing Services</p>
      <p>SMS, VB, SMM, SEM,</p>
    </div>
    <div class="reach-address">
      <p>247 E. Pelham Row, 5th Floor, San Diego CA 92384</p>
      <p>www.<span class="site-name">BrightlaneReach</span>.com</p>
    </div>
    <div class="reach-rule reach-rule--foot"></div>
  </section>

</main>
</body>
</html>
```